Bref créative
Brookmere
Brookmere Vale Baptist Church
Simple
Dolores Lomax
Communications
4163 Ambervale Road
Hollin Bay HB S7N 3K8
dolores@brookmerechapel.ca
brookmerechapel.ca
We will need business cards, letterhead and envelopes.
Our Logo
ai file

```html
<!DOCTYPE html>
<html lang="en">
<head>
<meta charset="utf-8">
<title>Brookmere Vale Baptist Church – Envelope</title>
<link rel="stylesheet" href="https://fonts.googleapis.com/css2?family=Cinzel:wght@400;600&family=Open+Sans:wght@400;600&display=swap">
<style>
  :root {
    --backdrop: #e9eaec;
    --paper: #ffffff;
    --edge: #9a9da3;
    --fold: #d7d9dc;
    --brand-blue: #3d72a8;
    --ink-blue: #2f5f93;
    --accent-gold: #b8914a;
    --rule-grey: #a9adb3;
    --postage-grey: #c9ccd1;
    --photo-deep: #1d4f86;
    --photo-light: #8fb8dd;
  }
  html, body {
    margin: 0;
    padding: 0;
    width: 1200px;
    height: 869px;
    overflow: hidden;
    background: var(--backdrop);
  }
  .envelope {
    position: relative;
    width: 1200px;
    height: 869px;
  }
  .envelope-shape {
    position: absolute;
    inset: 0;
  }
  .return-address {
    position: absolute;
    left: 158px;
    top: 344px;
    font-family: "Open Sans", Arial, sans-serif;
  }
  .brand-name {
    margin: 0 0 42px;
    font-family: "Cinzel", "Times New Roman", serif;
    font-weight: 400;
    font-size: 29px;
    letter-spacing: 0.5px;
    line-height: 1;
    color: var(--brand-blue);
  }
  .contact-line {
    margin: 0;
    font-size: 11.5px;
    line-height: 18px;
    color: var(--ink-blue);
  }
  .contact-line.web { color: var(--accent-gold); }
  .postage-box {
    position: absolute;
    left: 962px;
    top: 350px;
    width: 104px;
    height: 116px;
    box-sizing: border-box;
    border: 2px solid var(--postage-grey);
    display: flex;
    align-items: center;
    justify-content: center;
    text-align: center;
    font-family: "Open Sans", Arial, sans-serif;
    font-size: 19px;
    line-height: 22px;
    color: var(--postage-grey);
    text-transform: uppercase;
  }
  .flap-mark {
    position: absolute;
    left: 708px;
    top: 212px;
    transform: rotate(180deg);
    font-family: "Cinzel", "Times New Roman", serif;
    font-size: 15px;
    color: var(--brand-blue);
    letter-spacing: 0.5px;
  }
</style>
</head>
<body>
<main class="envelope">
  <svg class="envelope-shape" width="1200" height="869" viewBox="0 0 1200 869">
    <defs>
      <linearGradient id="flapPhotoTone" x1="0" y1="0" x2="1" y2="0">
        <stop offset="0" stop-color="var(--photo-light)"/>
        <stop offset="0.45" stop-color="var(--photo-deep)"/>
        <stop offset="1" stop-color="var(--photo-light)"/>
      </linearGradient>
    </defs>
    <path class="envelope-outline"
          d="M96 307 L600 137 L1109 307 L1109 773 L96 773 Z"
          fill="var(--paper)" stroke="var(--edge)" stroke-width="3"/>
    <line x1="96" y1="311" x2="1109" y2="311" stroke="var(--fold)" stroke-width="1.5"/>
    <path role="img" aria-label="Photograph of the church interior in blue tones"
          d="M408 202 L600 140 L792 202 Q700 218 600 212 Q500 206 408 202 Z"
          fill="url(#flapPhotoTone)"/>
    <path d="M408 202 Q500 206 600 212 Q700 218 792 202"
          fill="none" stroke="var(--accent-gold)" stroke-width="2"/>
    <g class="address-rules" stroke="var(--rule-grey)" stroke-width="1.5">
      <line x1="415" y1="547" x2="864" y2="547"/>
      <line x1="415" y1="567" x2="864" y2="567"/>
      <line x1="415" y1="588" x2="864" y2="588"/>
    </g>
  </svg>

  <div class="flap-mark">Brookmere</div>

  <section class="return-address">
    <h1 class="brand-name">Brookmere</h1>
    <p class="contact-line">4163 Ambervale Road, Hollin Bay HB S7N 3K8</p>
    <p class="contact-line">P: 555-210-0142</p>
    <p class="contact-line">F: 555-210-0187</p>
    <p class="contact-line web">brookmerechapel.ca</p>
  </section>

  <div class="postage-box">Place<br>Postage<br>Here</div>
</main>
</body>
</html>
```